salami paper bag design The size is 10.5cm 21.5cm 6.7cm

This time we need to make renew salami package design. Planning to make paper salami package. I tried to design but I couldnt formyself.
So please correct my design and recreate more nicer package design from my salami design that attach on the documents.
Logo part I am planning gold stamp. If anybody can make more nicer logo for the package,I don’t mind it.please change the color and shape and everything.
The size is 10.5cm 21.5cm 6.7cm
Thank you.

Target Market(s)

uper market make costomer feel luxurious

Industry/Entity Type

salami matured meat products

Font styles to use
Sans Serif
Decorative
Script

Colors

Designer to choose colors to be used in the design.

Requirements
Nice to have
• Make customer feel joy for genuine fermented salami with wine
Should not have
• My projrct must not have cheap discount design.

```html
<!DOCTYPE html>
<html lang="en">
<head>
<meta charset="utf-8">
<title>Morindal Handmade Salami – Bag Front</title>
<link rel="stylesheet" href="https://fonts.googleapis.com/css2?family=Libre+Caslon+Text:wght@400;700&family=Lobster&family=Noto+Sans+JP:wght@400;500&display=swap">
<style>
  :root {
    --backdrop: #a6d2de;
    --bag-black: #242326;
    --gold: #d9b216;
    --gold-deep: #b8930c;
    --banner-red: #e3262c;
    --white: #ffffff;
  }
  * { box-sizing: border-box; margin: 0; padding: 0; }
  html, body {
    width: 1200px; height: 900px; overflow: hidden;
    background: var(--backdrop);
  }
  .canvas { position: relative; width: 1200px; height: 900px; }
  .bag-front {
    position: absolute; left: 395px; top: 30px;
    width: 410px; height: 840px;
    background: var(--bag-black);
    color: var(--gold);
    font-family: "Libre Caslon Text", Georgia, serif;
    overflow: hidden;
  }
  .crest {
    position: absolute; left: 74px; top: 91px;
    width: 262px; height: 170px;
    background: radial-gradient(ellipse at 50% 45%, rgba(217,178,22,0.85) 0%, rgba(201,163,16,0.45) 45%, rgba(201,163,16,0.08) 75%, transparent 100%);
  }
  .crest-since {
    position: absolute; left: 0; top: 262px; width: 100%;
    text-align: center; font-size: 12px; letter-spacing: 0.5px;
  }
  .quality-arc {
    position: absolute; left: 105px; top: 298px; width: 200px; height: 40px;
  }
  .quality-arc text {
    font-family: "Libre Caslon Text", Georgia, serif;
    font-size: 12px; letter-spacing: 1px; fill: var(--gold);
  }
  .brand-name {
    position: absolute; left: 0; top: 340px; width: 100%;
    text-align: center;
    font-size: 66px; font-weight: 700; line-height: 1;
    color: var(--gold);
  }
  .since {
    position: absolute; left: 0; top: 432px; width: 100%;
    text-align: center; font-size: 15px; letter-spacing: 0.5px;
  }
  .ornament {
    position: absolute; top: 466px; width: 46px; height: 76px;
    background: linear-gradient(180deg, #e2bd20, #b8930c);
    border-radius: 45%;
  }
  .ornament--left { left: 21px; }
  .ornament--right { left: 344px; }
  .tagline {
    position: absolute; left: 76px; top: 471px;
    width: 260px; height: 70px;
    background: var(--banner-red);
    border: 3px solid var(--gold);
    outline: 2px solid var(--gold-deep);
    outline-offset: 2px;
    text-align: center; color: var(--white);
    padding-top: 6px;
  }
  .tagline-en {
    font-family: "Lobster", cursive;
    font-size: 24px; line-height: 1.1; letter-spacing: 0.5px;
  }
  .tagline-ja {
    font-family: "Noto Sans JP", sans-serif;
    font-size: 16px; line-height: 1.35; letter-spacing: 1px;
  }
  .window {
    position: absolute; left: 45px; top: 593px;
    width: 321px; height: 140px;
    background: var(--backdrop);
    border: 3px solid var(--gold);
    border-radius: 14px;
  }
  .window-label {
    position: absolute; left: 50%; transform: translateX(-50%);
    background: var(--gold); color: var(--bag-black);
    white-space: nowrap; line-height: 1;
  }
  .window-label--ja {
    top: -13px; padding: 4px 10px;
    font-family: "Noto Sans JP", sans-serif; font-size: 13px; letter-spacing: 1px;
  }
  .window-label--en {
    bottom: -15px; padding: 5px 10px;
    font-family: "Libre Caslon Text", Georgia, serif; font-size: 14px; letter-spacing: 0.3px;
  }
  .rope-band {
    position: absolute; left: 0; top: 776px;
    width: 100%; height: 64px;
    background: var(--gold);
  }
</style>
</head>
<body>
<main class="canvas">
  <section class="bag-front">
    <div class="crest" role="img" aria-label="Gold-stamped heraldic crest with crown, shield, laurel and flourishes"></div>
    <p class="crest-since">Since1951</p>

    <svg class="quality-arc" viewBox="0 0 200 40">
      <path id="quality-path" d="M10,36 Q100,2 190,36" fill="none"/>
      <text text-anchor="middle"><textPath href="#quality-path" startOffset="50%">SUPERIOR QUALITY</textPath></text>
    </svg>

    <h1 class="brand-name">Morindal</h1>
    <p class="since">Since1951</p>

    <div class="ornament ornament--left" role="img" aria-label="Gold filigree ornament"></div>
    <div class="tagline">
      <p class="tagline-en">SAVOUR EVERY DAY</p>
      <p class="tagline-ja">毎日をゆっくり味わう</p>
    </div>
    <div class="ornament ornament--right" role="img" aria-label="Gold filigree ornament"></div>

    <div class="window">
      <span class="window-label window-label--ja">手作りサラミ</span>
      <span class="window-label window-label--en">HANDMADE SALAMI</span>
    </div>

    <div class="rope-band" role="img" aria-label="Gold twisted-rope stripe pattern band"></div>
  </section>
</main>
</body>
</html>
```